Business Card and Letterhead for Nurlo - modern real estate business

I need a double sided business card design for Nurlo. Please see business card brief here https://papers.trelvimo.net/sheet/q/7XrTbaLeZpMmQ2uWvd9HkCj4yNoEfsGi3lRtAz_pk/view?mode=shared

Please feel free to design the business cards however you feel best. I am happy to give some creative freedoms and then provide feedback from there.

Please then also create a letterhead to match the business card design

Colors

Designer to choose colors to be used in the design.

Requirements
Must have
• Must be a modern, elegant business card which looks very professional

```html
<!DOCTYPE html>
<html lang="en">
<head>
<meta charset="utf-8">
<title>Nurlo – Stationery Set</title>
<link rel="stylesheet" href="https://fonts.googleapis.com/css2?family=Montserrat:wght@300;400;600;700;800&family=Jost:wght@400;500&display=swap">
<style>
  :root {
    --stage: #e9e9e9;
    --ink: #050505;
    --ink-soft: #0b0b0d;
    --brand-red: #e01b24;
    --deep-red: #6e1520;
    --paper: #ffffff;
    --muted: #6f6f6f;
    --body-text: #5a5a5a;
    --light-text: #c9c9c9;
    --photo-green: #7f8f63;
    --photo-suit: #2a2b2e;
  }
  * { margin: 0; padding: 0; box-sizing: border-box; }
  html, body { width: 1200px; height: 1200px; overflow: hidden; }
  body { background: var(--stage); position: relative; font-family: "Montserrat", sans-serif; }

  .piece { position: absolute; box-shadow: -8px 10px 14px rgba(0,0,0,0.28); overflow: hidden; }

  .wordmark { color: var(--brand-red); font-family: "Montserrat", sans-serif; font-weight: 600; letter-spacing: 0.02em; line-height: 1; }

  /* Business card front */
  .card-front {
    left: 107px; top: 108px; width: 394px; height: 243px;
    background: linear-gradient(180deg, #000 0%, #050303 55%, #1a0507 100%);
    display: flex; align-items: center; justify-content: center;
  }
  .card-front .wordmark { font-size: 36px; margin-top: -6px; }

  /* Business card back */
  .card-back { left: 696px; top: 109px; width: 394px; height: 243px; background: var(--ink); }
  .card-back svg.art { position: absolute; left: 0; top: 0; }
  .contact-block { position: absolute; right: 18px; top: 0; text-align: right; color: #fff; }
  .contact-row { position: absolute; right: 0; display: flex; align-items: center; gap: 10px; white-space: nowrap; }
  .icon-dot { width: 17px; height: 17px; border-radius: 50%; background: #fff; display: flex; align-items: center; justify-content: center; }
  .agent-name { top: 67px; font-size: 15px; font-weight: 300; letter-spacing: 0.03em; }
  .agent-name b { font-weight: 700; margin-left: 5px; }
  .agent-role { position: absolute; right: 27px; top: 90px; font-size: 11px; font-weight: 300; color: var(--light-text); line-height: 1.2; white-space: nowrap; }
  .phone-row { top: 128px; font-size: 11.5px; font-weight: 300; }
  .mail-row { top: 155px; font-size: 11.5px; font-weight: 300; }

  /* Letterhead */
  .letterhead { left: 89px; top: 506px; width: 392px; height: 553px; background: var(--paper); }
  .letterhead .wordmark { position: absolute; left: 54px; top: 27px; font-size: 15px; }
  .headline { position: absolute; left: 50px; top: 138px; font-size: 26px; font-weight: 800; color: var(--muted); letter-spacing: 0.01em; }
  .letter-body { position: absolute; left: 50px; top: 181px; width: 296px; font-family: "Jost", sans-serif; font-size: 7.4px; line-height: 10.2px; color: var(--body-text); }
  .letter-body p + p { margin-top: 10.2px; }
  .signature { position: absolute; right: 61px; top: 385px; text-align: right; font-family: "Jost", sans-serif; font-size: 7.4px; line-height: 9.8px; color: var(--body-text); }
  .signature .title { font-family: "Montserrat", sans-serif; font-weight: 700; color: var(--muted); font-size: 7px; }
  .signature .web { color: #9a9a9a; font-size: 6.6px; }
  .letter-footer { position: absolute; left: 0; bottom: 0; width: 392px; height: 23px; background: var(--ink); border-radius: 24px 24px 0 0 / 20px 20px 0 0; color: #fff; font-size: 10px; }
  .footer-item { position: absolute; top: 5px; display: flex; align-items: center; gap: 8px; }
  .footer-item .icon-dot { background: var(--brand-red); width: 14px; height: 14px; }
  .footer-phone { left: 61px; }
  .footer-mail { left: 232px; top: 4px; }

  /* Folder */
  .folder {
    left: 716px; top: 507px; width: 389px; height: 551px;
    background: linear-gradient(180deg, var(--ink-soft) 0%, #0b0b0d 45%, #140709 80%, #1c080b 100%);
  }
  .folder .wordmark { position: absolute; left: 0; right: 0; top: 254px; text-align: center; font-size: 33px; }
</style>
</head>
<body>

  <section class="piece card-front" aria-label="Business card front">
    <span class="wordmark">NURLO</span>
  </section>

  <section class="piece card-back" aria-label="Business card back">
    <svg class="art" width="394" height="243" viewBox="0 0 394 243">
      <defs>
        <linearGradient id="portraitTone" x1="0" y1="0" x2="0" y2="1">
          <stop offset="0" stop-color="var(--photo-green)"/>
          <stop offset="0.45" stop-color="#8f8a7c"/>
          <stop offset="0.7" stop-color="var(--photo-suit)"/>
          <stop offset="1" stop-color="#1e1f22"/>
        </linearGradient>
      </defs>
      <polygon role="img" aria-label="Portrait photo of the agent in a dark suit, outdoors" points="0,0 127,0 173,243 0,243" fill="url(#portraitTone)"/>
      <polygon points="127,0 139,0 180,243 173,243" fill="var(--brand-red)"/>
      <polygon points="139,0 151,0 188,243 180,243" fill="var(--deep-red)"/>
    </svg>
    <div class="contact-block">
      <div class="contact-row agent-name"><span>DANE<b>MARLOW</b></span>
        <span class="icon-dot"><svg width="9" height="9" viewBox="0 0 10 10"><circle cx="5" cy="3" r="2" fill="none" stroke="#000" stroke-width="1"/><path d="M1.5 9.5 Q5 5 8.5 9.5 Z" fill="none" stroke="#000" stroke-width="1"/></svg></span>
      </div>
    </div>
    <div class="agent-role">Licenced Real Estate Agent<br>Lic No. 20419386</div>
    <div class="contact-block">
      <div class="contact-row phone-row"><span>0412 300 918</span>
        <span class="icon-dot"><svg width="9" height="9" viewBox="0 0 10 10"><path d="M2 1 L3.6 1 L4.2 3 L3.2 3.8 Q4.2 5.8 6.2 6.8 L7 5.8 L9 6.4 L9 8 Q8.6 9 7.5 9 Q1 8 1 2.5 Q1 1 2 1 Z" fill="none" stroke="#000" stroke-width="0.9"/></svg></span>
      </div>
      <div class="contact-row mail-row"><span>dane@nurlo.com</span>
        <span class="icon-dot"><svg width="9" height="9" viewBox="0 0 10 10"><rect x="1" y="2.2" width="8" height="5.6" fill="none" stroke="#000" stroke-width="0.9"/><path d="M1 2.2 L5 5.4 L9 2.2" fill="none" stroke="#000" stroke-width="0.9"/></svg></span>
      </div>
    </div>
  </section>

  <section class="piece letterhead" aria-label="Letterhead">
    <span class="wordmark">NURLO</span>
    <h1 class="headline">HEADLINE</h1>
    <div class="letter-body">
      <p>Lorem ipsum dolor sit amet, consectetur adipiscing elit. Fusce dignissim pretium consectetur. Curabitur tempor posuere massa in varius. Pellentesque viverra nibh eu vehicula mattis. Nullam porta facilisis justo, a feugiat dolor sodales sed. Vestibulum neque nisi, elementum tincidunt metus sit amet, egestas bibendum enim. Aenean a blandit elit, vel rutrum mi. Nunc dapibus turpis sed massa aliquet tincidunt.</p>
      <p>Pellentesque id neque ligula. Nullam posuere, ligula a mattis posuere, lacus nisl adipiscing nunc, eu congue justo est ut diam. Nam quam nibh, dignissim non consequat in, semper eget purus. Nulla arcu sapien, viverra vitae metus tempor, congue ornare diam.</p>
      <p>Pellentesque vel nibh tempus, ullamcorper tortor sed, bibendum augue. Phasellus sollicitudin justo et quam aliquam sollicitudin. Sed eget nibh mollis, mattis sem et, viverra nulla.</p>
    </div>
    <div class="signature">
      <div class="title">Creative Art Director</div>
      <div>Pellentesque id neque ligula. Nullam posuere</div>
      <div class="web">www.companyname.com</div>
    </div>
    <footer class="letter-footer">
      <div class="footer-item footer-phone">
        <span class="icon-dot"><svg width="8" height="8" viewBox="0 0 10 10"><path d="M2 1 L3.6 1 L4.2 3 L3.2 3.8 Q4.2 5.8 6.2 6.8 L7 5.8 L9 6.4 L9 8 Q8.6 9 7.5 9 Q1 8 1 2.5 Q1 1 2 1 Z" fill="none" stroke="#fff" stroke-width="1"/></svg></span>
        <span>0412 300 918</span>
      </div>
      <div class="footer-item footer-mail">
        <span class="icon-dot"><svg width="8" height="8" viewBox="0 0 10 10"><rect x="1" y="2.2" width="8" height="5.6" fill="none" stroke="#fff" stroke-width="1"/><path d="M1 2.2 L5 5.4 L9 2.2" fill="none" stroke="#fff" stroke-width="1"/></svg></span>
        <span>dane@nurlo.com</span>
      </div>
    </footer>
  </section>

  <section class="piece folder" aria-label="Presentation folder cover">
    <span class="wordmark">NURLO</span>
  </section>

</body>
</html>
```